I want to revise my business card design and get a more modern and up to date design.

Brolvane Handyman Sevices originated from a family-owned and operated contractor business, performing home renovation, addition, and construction work in the NYC area since 2004. Today, we specialize in reliable and affordable handyman services for residential and commercial clients In 2014, we expanded to northern New Jersey. In 2016, we brought quality home improvement and repair services to new Bucks County, PA, and nearby New Jersey areas.
Target Market(s)
Home owners and business that might be looking for a General contractor, handyman, cleaning services and Home maintenance and property.
Industry/Entity Type
Construction Company
Contact Information for Business Card
I am open to new ideas
Colors
Designer to choose colors to be used in the design.
Look and feel
Each slider illustrates characteristics of the customer's brand and the style your logo design should communicate.

```html
<!DOCTYPE html>
<html lang="en">
<head>
<meta charset="utf-8">
<title>Brolvane Handyman Sevices – Business Card</title>
<link href="https://fonts.googleapis.com/css2?family=Roboto:wght@400;500;700;900&display=swap" rel="stylesheet">
<style>
  :root {
    --bg: #2a2c2f;
    --red: #e61c24;
    --yellow: #fdd22e;
    --black: #111111;
    --white: #ffffff;
    --ink: #1b1b1b;
  }
  * { margin: 0; padding: 0; box-sizing: border-box; }
  html, body { width: 1200px; height: 900px; overflow: hidden; }
  body {
    background: var(--bg);
    font-family: 'Roboto', Arial, sans-serif;
    position: relative;
  }
  .card {
    position: absolute;
    top: 296px;
    width: 540px;
    height: 308px;
    border-radius: 4px;
    overflow: hidden;
    box-shadow: 0 14px 30px rgba(0,0,0,.45);
  }
  .card-front { left: 40px; background: var(--white); }
  .card-back { left: 620px; }
  .card svg.art { position: absolute; inset: 0; }

  .contact-block { position: absolute; left: 30px; top: 28px; }
  .person-name {
    font-size: 30px; font-weight: 700; color: var(--ink); letter-spacing: -.2px;
  }
  .person-name .surname { color: var(--red); }
  .person-role {
    margin-top: 10px; font-size: 15px; line-height: 1.3; color: var(--ink);
  }
  .contact-list { list-style: none; margin-top: 14px; }
  .contact-list li {
    display: flex; align-items: center; gap: 8px;
    font-size: 15px; color: var(--ink); margin-bottom: 6px;
  }
  .contact-list svg { width: 14px; height: 14px; flex: none; }

  .service-band {
    position: absolute; left: 0; bottom: 64px;
    width: 300px; height: 34px; padding-left: 30px;
    display: flex; align-items: center;
    font-size: 15px; font-weight: 500; color: var(--white); letter-spacing: .3px;
  }

  .front-brand {
    position: absolute; right: 34px; top: 112px;
    display: flex; align-items: center; gap: 10px;
  }
  .brand-dot { width: 22px; height: 22px; border-radius: 50%; background: var(--red); }
  .brand-name { font-size: 26px; font-weight: 900; color: var(--ink); }

  .back-brand {
    position: absolute; left: 0; right: 0; top: 128px;
    display: flex; align-items: center; justify-content: center; gap: 12px;
  }
  .back-brand .brand-dot { background: var(--red); width: 26px; height: 26px; }
  .back-brand .brand-name { font-size: 30px; font-weight: 900; color: var(--black); }
</style>
</head>
<body>

  <section class="card card-front" aria-label="Business card front">
    <svg class="art" viewBox="0 0 540 308" aria-hidden="true">
      <polygon points="0,210 300,210 322,244 0,244" fill="var(--red)"/>
      <polygon points="322,244 540,120 540,308 400,308" fill="var(--black)"/>
    </svg>

    <div class="contact-block">
      <h1 class="person-name">Marco <span class="surname">Teixeira</span></h1>
      <p class="person-role">Commercial and Residential<br>Contractor, Handyman, Technician</p>
      <ul class="contact-list">
        <li>
          <svg viewBox="0 0 14 14"><rect x="3" y="1" width="8" height="12" rx="1.5" fill="none" stroke="var(--red)" stroke-width="1.6"/></svg>
          (215) 555-0148
        </li>
        <li>
          <svg viewBox="0 0 14 14"><rect x="1" y="3" width="12" height="8" fill="var(--red)"/><polyline points="1,3 7,8 13,3" fill="none" stroke="var(--white)" stroke-width="1.2"/></svg>
          brolvanehandyman@mail.com
        </li>
      </ul>
    </div>

    <div class="service-band" style="bottom:64px;">Repair &nbsp;|&nbsp; Improve &nbsp;|&nbsp; Maintain &nbsp;|&nbsp; Remodel</div>

    <div class="front-brand">
      <span class="brand-dot"></span>
      <span class="brand-name">Brolvane</span>
    </div>
  </section>

  <section class="card card-back" aria-label="Business card back">
    <svg class="art" viewBox="0 0 540 308" aria-hidden="true">
      <rect width="540" height="308" fill="var(--yellow)"/>
      <polygon points="0,0 540,0 540,70 0,40" fill="var(--red)"/>
      <polygon points="0,250 540,268 540,308 0,308" fill="var(--black)"/>
    </svg>
    <div class="back-brand">
      <span class="brand-dot"></span>
      <span class="brand-name">Brolvane Handyman Sevices</span>
    </div>
  </section>

</body>
</html>
```